Business Card Design

I need a business card design for a new business based in South West Australia.
I specialize in residential window cleaning & general handyman maintenance.

Industry/Entity Type

Business

Contact Information for Business Card

Dean Harlow - 482 SILVER HAWK DETAILING
- Window Cleaning
- House Maintenance

```html
<!DOCTYPE html>
<html lang="en">
<head>
<meta charset="utf-8">
<title>482 Silver Hawk Detailing – Business Card</title>
<link href="https://fonts.googleapis.com/css2?family=Josefin+Sans:wght@600;700&family=Barlow:wght@500&display=swap" rel="stylesheet">
<style>
  :root {
    --page-bg: #1d2631;
    --sky-light: #1fbcee;
    --sky-mid: #0a8fd6;
    --sky-deep: #0562b3;
    --grass-light: #b3cd5a;
    --grass-deep: #8fb23c;
    --ink: #111111;
    --white: #ffffff;
  }
  html, body {
    margin: 0;
    width: 1200px;
    height: 1200px;
    overflow: hidden;
    background: var(--page-bg);
  }
  .business-card {
    position: absolute;
    left: 50px;
    top: 280px;
    width: 1100px;
    height: 640px;
    overflow: hidden;
    box-shadow: 0 20px 50px rgba(0,0,0,0.45);
  }
  .card-art { position: absolute; inset: 0; }
  .brand-mark {
    position: absolute;
    left: 60px;
    top: 70px;
    width: 230px;
    text-align: center;
    font-family: "Barlow", sans-serif;
    font-weight: 500;
    font-size: 26px;
    line-height: 1.2;
    color: var(--white);
  }
  .brand-mark .mark-dot {
    display: block;
    width: 70px;
    height: 70px;
    margin: 0 auto 20px;
    border-radius: 50%;
    background: var(--white);
  }
  .company-name {
    position: absolute;
    left: 340px;
    top: 70px;
    margin: 0;
    font-family: "Josefin Sans", sans-serif;
    font-weight: 600;
    font-size: 56px;
    line-height: 1.12;
    color: var(--white);
    letter-spacing: 1px;
  }
  .services {
    position: absolute;
    left: 345px;
    top: 210px;
    display: flex;
    gap: 28px;
    font-family: "Barlow", sans-serif;
    font-weight: 500;
    font-size: 31px;
    color: var(--ink);
  }
  .services span { display: flex; align-items: center; gap: 16px; }
  .icon { width: 28px; height: 28px; fill: var(--ink); flex: none; }
  .person-name {
    position: absolute;
    left: 80px;
    top: 405px;
    margin: 0;
    font-family: "Barlow", sans-serif;
    font-weight: 500;
    font-size: 64px;
    color: var(--ink);
  }
  .contact-line {
    position: absolute;
    display: flex;
    align-items: center;
    gap: 14px;
    font-family: "Barlow", sans-serif;
    font-weight: 500;
    color: var(--ink);
  }
  .phone { left: 100px; top: 500px; font-size: 42px; }
  .address { left: 560px; top: 425px; font-size: 31px; }
  .email { left: 560px; top: 478px; font-size: 31px; }
</style>
</head>
<body>
  <div class="business-card">
    <svg class="card-art" viewBox="0 0 1100 640" aria-hidden="true">
      <defs>
        <radialGradient id="sky" cx="0.12" cy="0.35" r="1">
          <stop offset="0" stop-color="var(--sky-light)"/>
          <stop offset="0.5" stop-color="var(--sky-mid)"/>
          <stop offset="1" stop-color="var(--sky-deep)"/>
        </radialGradient>
        <linearGradient id="grass" x1="0" y1="0" x2="0" y2="1">
          <stop offset="0" stop-color="var(--grass-light)"/>
          <stop offset="1" stop-color="var(--grass-deep)"/>
        </linearGradient>
      </defs>
      <rect width="1100" height="640" fill="url(#sky)"/>
      <path d="M0 345 Q380 300 700 320 L1100 275 L1100 640 L0 640 Z" fill="url(#grass)"/>
      <path d="M700 320 L1100 275 L1100 395 Q930 330 700 320 Z" fill="var(--grass-light)"/>
      <path d="M0 345 Q380 300 700 320 L1100 275" fill="none" stroke="var(--white)" stroke-width="6"/>
    </svg>

    <div class="brand-mark"><span class="mark-dot"></span>482 SILVER HAWK DETAILING</div>

    <h1 class="company-name">482 SILVER HAWK<br>DETAILING</h1>

    <div class="services">
      <span><svg class="icon" viewBox="0 0 24 24"><path d="M12 2 1 12h3v10h6v-6h4v6h6V12h3z"/></svg>Window Cleaning</span>
      <span><svg class="icon" viewBox="0 0 24 24"><path d="M12 2 1 12h3v10h6v-6h4v6h6V12h3z"/></svg>House Maintenance</span>
    </div>

    <h2 class="person-name">Dean Harlow</h2>

    <div class="contact-line phone">
      <svg class="icon" viewBox="0 0 24 24"><path d="M6.6 10.8a15.1 15.1 0 0 0 6.6 6.6l2.2-2.2c.3-.3.7-.4 1-.2 1.1.4 2.3.6 3.6.6.6 0 1 .4 1 1V20c0 .6-.4 1-1 1A17 17 0 0 1 3 4c0-.6.4-1 1-1h3.5c.6 0 1 .4 1 1 0 1.3.2 2.5.6 3.6.1.3 0 .7-.2 1z"/></svg>
      041 26 870 54
    </div>
    <div class="contact-line address">
      <svg class="icon" viewBox="0 0 24 24"><path d="M12 3 2 12h3v8h5v-5h4v5h5v-8h3z"/></svg>
      #00, Adress 01, Line 02.
    </div>
    <div class="contact-line email">
      <svg class="icon" viewBox="0 0 24 24"><path d="M12 2a10 10 0 1 0 0 20 10 10 0 0 0 0-20zm6.9 6h-2.9a15.7 15.7 0 0 0-1.4-3.6A8 8 0 0 1 18.9 8zM12 4c.8 1.2 1.5 2.5 1.9 4h-3.8c.4-1.4 1.1-2.8 1.9-4zM4.3 14a8 8 0 0 1 0-4h3.4a16 16 0 0 0 0 4zm.8 2h2.9c.3 1.3.8 2.5 1.4 3.6A8 8 0 0 1 5.1 16zM8 8H5.1a8 8 0 0 1 4.3-3.6C8.8 5.5 8.4 6.7 8 8zm4 12c-.8-1.2-1.5-2.5-1.9-4h3.8c-.4 1.4-1.1 2.8-1.9 4zm2.3-6H9.7a14 14 0 0 1 0-4h4.6a14 14 0 0 1 0 4zm.3 5.6c.6-1.1 1.1-2.3 1.4-3.6h2.9a8 8 0 0 1-4.3 3.6zm1.8-5.6a16 16 0 0 0 0-4h3.4a8 8 0 0 1 0 4z"/></svg>
      info@silverhawkdetailing.au
    </div>
  </div>
</body>
</html>
```